Zielgruppe
Wir sind eine Event-Agentur im Westen Berlins mit dem Teilschwerpunkt 'Medizin'. Zu unseren Kunden gehören namenhafte Krankenhäuser, Ärzte und Organisationen welche Fortbildungsveranstaltungen bei uns organisieren lassen. Unsere Zielgruppe sind Ärzte und medizinisches Personal, welche an unseren Events teilnehmen um auf dem neusten Stand der Medizin, Hygiene und anderen Themen zu bleiben.
Aufgabenstellung
UPDATE: Unser Chef wünscht sich, dass der Fokus nicht nur auf dem Thema Arthroskopie liegt, sondern schon eher in Richtung 'Gelenke' gehen soll. Bitte entsprechend beachten!
Wir benötigen ein Design für einen DIN lang Flyer, welches gleichzeitig modern und doch nicht zu flippig ist. Das Design muss den Spagat zwischen Technik und Menschlichkeit widerspiegeln. Farblich sind keine Vorgaben vorhanden. Ob mit Stock Fotos, graphischen Elementen oder mit typographischem Design: wir sind für alle Vorschläge offen.
Thematisch geht es um die Bewerbung einer Veranstaltung im orthopädischen Sektor (falls für Ihr Design relevant: es handelt sich um Arthroskopien). Das Design soll so angelegt sein, dass es im nächsten Jahr abgewandelt wiederverwendet werden kann ohne dass der Wiedererkennungswert verloren geht.
Folgende Texte müssen vorhanden sein:
'Veltrana-Symposium 2019' (Name der Veranstaltung)
'Neues aus der Schulter- und Kniearthroskopie' (Thema der Veranstaltung)
'21. bis 23. Februar 2019' (Datum)
'Krankenhaus Berlin' (Ort, leider noch mit Platzhalter)
Nice To Have, aber kein Muss: die Jahreszahl des jeweiligen Jahres könnte immer an der gleichen Stelle erscheinen. Für die nächste VA stünde dort 2019, aber für das darauffolgende Jahr 2020. Allerdings nur ein Gedanke von uns und kein Pflichtelement. Lieber nicht nutzen, falls es das Design irgendwie beeinträchtigt.
Falls Stockbilder dann bitte im erschwinglichen Rahmen vorschlagen! Das schönste Bild hilft uns nicht wenn es 50€ für 200x200 px kostet ;)
Vielen Dank im Voraus für Ihre Vorschläge!

```html
<!DOCTYPE html>
<html lang="de">
<head>
<meta charset="utf-8">
<title>Veltrana-Symposium 2019 – DIN lang Flyer</title>
<link rel="stylesheet" href="https://fonts.googleapis.com/css2?family=Saira:wght@300;400&family=Rubik:wght@400;700&display=swap">
<style>
  :root {
    --page-bg: #e9e7e3;
    --strip: #050708;
    --cyan: #1ec3ee;
    --white: #ffffff;
    --photo-dark: #050c12;
    --photo-mid: #0f2a3a;
    --lamp: #dfe6ec;
    --lamp-rim: #6f8796;
    --scrubs: #3f7f9e;
    --scrubs-deep: #1d4a63;
    --skin: #d89a72;
    --cap: #b89468;
  }
  * { margin: 0; padding: 0; box-sizing: border-box; }
  html, body { width: 1200px; height: 688px; overflow: hidden; }
  body { background: var(--page-bg); position: relative; }

  .flyer {
    position: absolute;
    left: 439px; top: 24px;
    width: 322px; height: 640px;
    background: var(--strip);
    overflow: hidden;
    box-shadow: 0 6px 18px rgba(0,0,0,0.25);
  }
  .flyer__strip {
    position: absolute; left: 0; top: 0;
    width: 62px; height: 100%;
    background: var(--strip);
  }
  .flyer__title { position: absolute; left: 0; top: 0; width: 62px; height: 640px; }
  .flyer__title text {
    font-family: "Saira", sans-serif;
    font-weight: 300;
    fill: var(--cyan);
  }
  .flyer__photo {
    position: absolute; left: 62px; top: 0; right: 0; bottom: 0;
    background:
      radial-gradient(ellipse 30% 14% at 22% 58%, var(--cap), transparent 75%),
      radial-gradient(ellipse 24% 12% at 55% 52%, var(--scrubs), transparent 75%),
      radial-gradient(ellipse 38% 14% at 20% 93%, var(--skin), transparent 75%),
      radial-gradient(ellipse 26% 10% at 48% 72%, #c9ccd0, transparent 75%),
      radial-gradient(ellipse 60% 28% at 62% 78%, var(--scrubs), transparent 78%),
      radial-gradient(ellipse 75% 32% at 55% 85%, var(--scrubs-deep), transparent 80%),
      radial-gradient(circle 62px at 20% 25%, var(--lamp), var(--lamp-rim) 60%, transparent 78%),
      radial-gradient(circle 78px at 88% 39%, var(--lamp), var(--lamp-rim) 60%, transparent 78%),
      linear-gradient(180deg, var(--photo-dark) 0%, var(--photo-mid) 55%, var(--photo-dark) 100%);
  }
  .flyer__year {
    position: absolute; right: 0; top: 0;
    width: 160px; height: 66px;
    background: var(--cyan);
    color: var(--white);
    font-family: "Saira", sans-serif;
    font-weight: 400;
    font-size: 54px; line-height: 66px;
    text-align: center;
    letter-spacing: 1px;
  }
  .flyer__meta {
    position: absolute; right: 8px; top: 70px;
    text-align: right;
    color: var(--cyan);
    font-family: "Rubik", sans-serif;
    font-weight: 400;
    font-size: 14px; line-height: 19px;
  }
  .flyer__meta .venue { font-size: 16px; }
  .flyer__topic {
    position: absolute; left: 68px; bottom: 12px;
    font-family: "Rubik", sans-serif;
    font-weight: 700;
    font-size: 18.5px; line-height: 22px;
    text-transform: uppercase;
    color: var(--white);
    text-shadow: 0 1px 4px rgba(0,0,0,0.6);
  }
  .flyer__topic .lead { color: var(--cyan); display: block; }
</style>
</head>
<body>
  <article class="flyer">
    <div class="flyer__strip"></div>
    <div class="flyer__photo" role="img" aria-label="Foto: zwei Chirurgen in blauer OP-Kleidung bei einer Kniearthroskopie unter runden OP-Leuchten"></div>

    <svg class="flyer__title" viewBox="0 0 62 640" aria-label="Veltrana-Symposium">
      <text x="0" y="0" transform="translate(52 622) rotate(-90)" font-size="54"
            textLength="600" lengthAdjust="spacingAndGlyphs">VELTRANA-SYMPOSIUM</text>
    </svg>

    <div class="flyer__year">2019</div>
    <div class="flyer__meta">
      <p class="date">21. bis 23. Februar 2019</p>
      <p class="venue">Krankenhaus Berlin</p>
    </div>

    <h1 class="flyer__topic">
      <span class="lead">Neues</span>
      aus der Schulter-<br>und Kniearthroskopie
    </h1>
  </article>
</body>
</html>
```